handmade items - handpainted and vinyl signs, hoodies, wood burned products (sold mostly at craft sales)
custom work available
home decor

Target Market(s)

woman - moms

Industry/Entity Type

craft shows

Logo Text

Pine Hollow Makers - Jenna Marsh & Brenda Okafor (with phone numbers)

Logo styles of interest
Emblem Logo
Pictorial/Combination Logo
Abstract Logo
Font styles to use
Decorative
Script

Requirements
Must have
• grain elevator
Nice to have
• train tracks

```html
<!DOCTYPE html>
<html lang="en">
<head>
<meta charset="utf-8">
<title>Pine Hollow Makers – Business Cards</title>
<link href="https://fonts.googleapis.com/css2?family=Cinzel:wght@400;700&display=swap" rel="stylesheet">
<style>
  :root {
    --stage: #2b2b2b;
    --ink: #141414;
    --rule: #1a1a1a;
    --paper: #f4f4f4;
    --sky-pale: #f6f6f6;
    --haze: #dedede;
    --ground-pale: #c4c4c4;
    --tower-pale: #b5b5b5;
    --sky-grey: #cfcfcf;
    --tower-dark: #3a3a3a;
    --trees: #5e5e5e;
    --ground-dark: #4a4a4a;
  }
  * { box-sizing: border-box; margin: 0; padding: 0; }
  html, body {
    width: 1200px; height: 1108px; overflow: hidden;
    background: var(--stage);
    font-family: "Cinzel", "Trajan Pro", serif;
    color: var(--ink);
  }
  .stage {
    position: relative; width: 1200px; height: 1108px;
    display: flex; justify-content: center; align-items: center; gap: 100px;
  }
  .card {
    position: relative; width: 400px; height: 690px;
    border-radius: 16px; overflow: hidden; background: var(--paper);
    box-shadow: 0 10px 30px rgba(0,0,0,.45);
  }
  .card__photo { position: absolute; inset: 0; width: 100%; height: 100%; }

  /* Front */
  .front__rule { position: absolute; left: 50%; width: 1px; background: var(--rule); }
  .front__rule--top { top: 0; height: 236px; }
  .front__rule--tick { top: 356px; height: 14px; }
  .front__rule--bottom { top: 480px; bottom: 0; }
  .front__text { position: absolute; left: 0; right: 0; top: 248px; text-align: center; }
  .brand-name { font-weight: 400; font-size: 36px; line-height: 1.1; letter-spacing: 2px; }
  .brand-name__spaced { display: block; letter-spacing: 16px; margin-right: -16px; }
  .front__owners { margin-top: 34px; font-weight: 700; font-size: 23px; letter-spacing: 1px; }
  .front__phone { margin-top: 2px; font-size: 22px; letter-spacing: 1px; }

  /* Back */
  .back__panel {
    position: absolute; top: 22px; right: 24px; bottom: 40px;
    writing-mode: vertical-rl;
    display: flex; flex-direction: column; gap: 10px;
  }
  .back__title {
    display: flex; align-items: center; gap: 10px;
    font-weight: 400; font-size: 19px; letter-spacing: 2px; white-space: nowrap;
    inline-size: 100%;
  }
  .back__title::before { content: ""; inline-size: 18px; block-size: 1px; background: var(--rule); }
  .back__title::after { content: ""; flex: 1; block-size: 1px; background: var(--rule); }
  .back__services {
    list-style: none; font-size: 12px; letter-spacing: 1px; line-height: 1.45;
    white-space: nowrap; padding-top: 28px;
  }
</style>
</head>
<body>
<main class="stage">
  <section class="card card--front">
    <svg class="card__photo" role="img" aria-label="Photo area: faded black and white grain elevator beside train tracks" viewBox="0 0 400 690" preserveAspectRatio="none">
      <defs>
        <linearGradient id="front-base" x1="0" y1="0" x2="0" y2="1">
          <stop offset="0" stop-color="var(--sky-pale)"/>
          <stop offset=".6" stop-color="var(--haze)"/>
          <stop offset="1" stop-color="var(--ground-pale)"/>
        </linearGradient>
        <filter id="front-soft"><feGaussianBlur stdDeviation="22"/></filter>
      </defs>
      <rect width="400" height="690" fill="url(#front-base)"/>
      <g filter="url(#front-soft)" opacity=".7">
        <rect x="40" y="110" width="150" height="340" fill="var(--tower-pale)"/>
        <rect x="0" y="520" width="400" height="170" fill="var(--ground-pale)"/>
      </g>
    </svg>
    <span class="front__rule front__rule--top"></span>
    <span class="front__rule front__rule--tick"></span>
    <span class="front__rule front__rule--bottom"></span>
    <div class="front__text">
      <h1 class="brand-name">PINE HOLLOW<span class="brand-name__spaced">MAKERS</span></h1>
      <p class="front__owners">JENNA AND BRENDA</p>
      <p class="front__phone">P:000.0000.000</p>
    </div>
  </section>

  <section class="card card--back">
    <svg class="card__photo" role="img" aria-label="Photo area: black and white grain elevator beside railway tracks under a cloudy sky" viewBox="0 0 400 690" preserveAspectRatio="none">
      <defs>
        <linearGradient id="back-base" x1="0" y1="0" x2="0" y2="1">
          <stop offset="0" stop-color="var(--sky-grey)"/>
          <stop offset=".55" stop-color="var(--haze)"/>
          <stop offset="1" stop-color="var(--ground-dark)"/>
        </linearGradient>
        <filter id="back-soft"><feGaussianBlur stdDeviation="20"/></filter>
      </defs>
      <rect width="400" height="690" fill="url(#back-base)"/>
      <g filter="url(#back-soft)">
        <rect x="0" y="40" width="190" height="420" fill="var(--tower-dark)" opacity=".8"/>
        <rect x="250" y="330" width="140" height="180" fill="var(--trees)" opacity=".5"/>
        <rect x="0" y="520" width="400" height="170" fill="var(--ground-dark)" opacity=".8"/>
      </g>
    </svg>
    <div class="back__panel">
      <h2 class="back__title">PINE HOLLOW MAKERS</h2>
      <ul class="back__services">
        <li>HANDPAINTED AND VINYL SIGNS</li>
        <li>HOODIES</li>
        <li>WOOD BURNED PRODUCTS</li>
      </ul>
    </div>
  </section>
</main>
</body>
</html>
```